Business broker needs designs for business card, letterhead and email signature

I require the following items:
- business cards
- letterhead
- email signature

My company is a Business Broker company that specialises in business sales across various industries. The company has branches in four areas and each area has its own logo and website. Initially for the submission I am happy to inspect 1 design and 1 layout for quillharborgroup but the winner will need to complete a design for each area.

The four areas are:
1. quillharborgroup
2. tealridgefuelsales
3. orbvalechainsales
4. pondgrovegrocerdeals

I would like one design for each of the above items for each area. In each design, there should be one prominent logo and then the remaining three should also be included, for eg, the letterhead for the quillharborgrp area would have the quillharborgrp logo featuring prominently, somewhere at the top perhaps and the logos of the other three areas would be smaller and perhaps at the bottom, down the side, etc.

For the business cards, one prominent logo should feature on one side with the remaining three logos on the reverse.

The overall objective is for each item to look like it belongs to one family . I need all the source files as I may add new industries moving forward.

Target Market(s)

My company targets business minded people looking to increase wealth,. make an investment or migrate to Australia. People who busy and are looking for efficient and professional service in securing their next business venture.

Industry/Entity Type

Business

Font styles to use
Serif
Sans Serif

Requirements
Must have
• I want something professional and corporate looking, not something cartoony or playful. I am happy for you to be creative.

```html
<!DOCTYPE html>
<html lang="en">
<head>
<meta charset="utf-8">
<title>quillharborgroup stationery</title>
<link rel="stylesheet" href="https://fonts.googleapis.com/css2?family=Questrial&display=swap">
<style>
:root{
  --stage:#cfcfcf;
  --paper:#f4f4f4;
  --slate:#34444e;
  --red:#d0112b;
  --ink:#4a4f55;
  --orange:#ee9a16;
  --teal:#18aeb0;
  --green:#3aa12f;
  --rule:#b9bcbf;
}
*{box-sizing:border-box;margin:0;padding:0}
html,body{width:1200px;height:900px;overflow:hidden}
body{background:var(--stage);font-family:"Questrial",sans-serif;color:var(--ink);position:relative}
.sheet{position:absolute;background:var(--paper)}
.brand{display:flex;align-items:center;gap:6px;white-space:nowrap}
.brand .mark{display:inline-block;background:var(--red)}
.brand .name{color:var(--slate)}
.band{position:absolute;top:0;height:6px}
.band.red{background:var(--red)}
.band.slate{background:var(--slate)}

/* letterhead */
.letterhead{left:220px;top:52px;width:383px;height:540px}
.letterhead .band.red{left:0;width:235px}
.letterhead .band.slate{left:239px;right:0}
.letterhead .head-brand{position:absolute;left:38px;top:38px}
.letterhead .head-brand .mark{width:18px;height:18px}
.letterhead .head-brand .name{font-size:16px}
.contact{position:absolute;left:257px;top:36px;font-size:5.4px;line-height:7.4px}
.contact li{list-style:none;display:flex;align-items:center;gap:4px}
.contact .ico{width:5px;height:5px;background:var(--red);display:inline-block}
.contact .addr{margin-top:4px}
.letter{position:absolute;left:36px;top:90px;width:311px;font-size:5.6px;line-height:6.9px;color:#5b6066}
.letter .date{margin-bottom:8px}
.letter .recipient{margin-bottom:50px}
.letter .salute{font-weight:bold;margin-bottom:8px;color:var(--ink)}
.letter p.body{text-align:justify;margin-bottom:7px}
.letter .signoff{margin-top:10px}
.letter .signer{color:var(--ink)}
.signature{position:absolute;left:90px;top:380px;width:80px;height:42px;background:linear-gradient(90deg,rgba(70,95,190,.12),rgba(70,95,190,.25),rgba(70,95,190,.1))}
.fold-mark{position:absolute;left:0;width:16px;height:1px;background:#dcdcdc}
.area-strip{position:absolute;left:30px;right:30px;display:flex;justify-content:space-between;align-items:center}
.area-strip .brand{gap:4px}
.area-strip .sep{width:1px;height:10px;background:var(--rule)}
.area-strip .name{font-size:8px}
.area-strip .mark{width:8px;height:8px}
.letterhead .area-strip{top:512px}
.footnote{position:absolute;left:0;right:0;bottom:0;height:10px;background:#bdbdbd;color:#eee;font-size:4.3px;line-height:10px;text-align:center}
.is-orange .mark{background:var(--orange)} .is-orange .name{color:var(--orange)}
.is-teal .mark{background:var(--teal)} .is-teal .name{color:var(--teal)}
.is-green .mark{background:var(--green)} .is-green .name{color:var(--green)}

/* folder */
.folder{left:649px;top:40px;width:416px;height:553px;background:var(--slate);border-radius:4px}
.folder .brand{position:absolute;left:117px;top:78px}
.folder .mark{width:30px;height:30px}
.folder .name{color:#fff;font-size:23px}

/* business cards */
.card{left:78px;width:164px;height:92px}
.card-front{top:637px}
.card-front .band.red{left:0;width:118px;height:3px}
.card-front .band.slate{left:121px;right:0;height:3px}
.card-front .brand{position:absolute;left:11px;top:15px}
.card-front .mark{width:10px;height:10px}
.card-front .name{font-size:8.5px}
.card-front .person{position:absolute;left:11px;top:46px;font-size:5px;color:var(--red)}
.card-front .person small{display:block;color:#777;font-size:3.6px}
.card-front .c-left{position:absolute;left:11px;top:69px;font-size:3.8px;line-height:5px}
.card-front .c-right{position:absolute;right:10px;top:69px;font-size:3.8px;line-height:5px;text-align:right}
.card-back{top:747px;background:var(--slate)}
.card-back .grid{position:absolute;inset:14px 10px;display:grid;grid-template-columns:1fr 1fr;grid-template-rows:1fr 1fr;align-items:center}
.card-back .brand{gap:3px}
.card-back .mark{width:6px;height:6px}
.card-back .name{font-size:5.6px}
.card-back .is-main .name{color:#fff}
.card-back .divider-v{position:absolute;left:82px;top:12px;bottom:12px;width:1px;background:rgba(255,255,255,.15)}
.card-back .divider-h{position:absolute;top:46px;left:10px;right:10px;height:1px;background:rgba(255,255,255,.15)}

/* envelopes */
.envelope{top:639px;width:400px;height:200px}
.envelope-front{left:277px}
.envelope-front .band.red{left:0;width:236px}
.envelope-front .band.slate{left:240px;right:0}
.envelope-front .brand{position:absolute;left:21px;top:30px}
.envelope-front .mark{width:17px;height:17px}
.envelope-front .name{font-size:13px}
.envelope-front .ret{position:absolute;left:42px;top:53px;font-size:5px;line-height:6.4px}
.envelope-back{left:724px}
.envelope-back .flap{position:absolute;left:0;top:0;width:400px;height:57px}
.envelope-back .flap-mark{position:absolute;left:193px;top:20px;width:14px;height:14px;background:var(--red)}
.envelope-back .area-strip{top:171px;left:40px;right:40px}
</style>
</head>
<body>

<!-- Letterhead -->
<section class="sheet letterhead">
  <div class="band red"></div><div class="band slate"></div>
  <div class="brand head-brand"><span class="mark"></span><span class="name">quillharborgroup</span></div>
  <ul class="contact">
    <li><span class="ico"></span>1300 555 018</li>
    <li><span class="ico"></span>info@quillharborgroup.example</li>
    <li><span class="ico"></span>www.quillharborgroup.example</li>
    <li class="addr">Level 12, Harbor Point,</li>
    <li>88 Quay Lane, Sydney NSW 2000</li>
    <li>ACN: 512 408 733</li>
  </ul>
  <div class="fold-mark" style="top:194px"></div>
  <div class="fold-mark" style="top:382px"></div>
  <div class="letter">
    <p class="date">30.02.2015</p>
    <p class="recipient">Recipient's name<br>Lindenweg 4<br>10115 Berlin<br>Germany</p>
    <p class="salute">Dear sir,</p>
    <p class="body">Thank you for your interest in our brokerage services. We help buyers and sellers move through each step of a business sale with care, clear advice and steady communication from first meeting to settlement.</p>
    <p class="body">Our team reviews every listing in detail, prepares accurate valuations and introduces qualified buyers who are ready to act. We keep records of each offer and discussion so that you always know where your sale stands.</p>
    <p class="body">Whether you plan to invest, expand or settle in a new city, we match you with businesses that suit your goals and budget. Each file is handled by a licensed agent who knows the local market well.</p>
    <p class="body">Please contact our office at any time to arrange a private meeting. We look forward to helping you secure your next venture.</p>
    <p class="signoff">Yours Sincerely,<br><strong class="signer">Tobin Merrow</strong></p>
  </div>
  <div class="signature" role="img" aria-label="Handwritten signature in blue ink"></div>
  <div class="area-strip">
    <div class="brand is-orange"><span class="mark"></span><span class="name">orbvalechainsales</span></div>
    <span class="sep"></span>
    <div class="brand is-teal"><span class="mark"></span><span class="name">tealridgefuelsales</span></div>
    <span class="sep"></span>
    <div class="brand is-green"><span class="mark"></span><span class="name">pondgrovegrocerdeals</span></div>
  </div>
  <div class="footnote">Licensed Business Broker and Real Estate Agent Lic No. 20118760, Buyers Agent. Member of Southland Guild of Business Agents (SGBA)</div>
</section>

<!-- Presentation folder -->
<section class="sheet folder">
  <div class="brand"><span class="mark"></span><span class="name">quillharborgroup</span></div>
</section>

<!-- Business card front -->
<section class="sheet card card-front">
  <div class="band red"></div><div class="band slate"></div>
  <div class="brand"><span class="mark"></span><span class="name">quillharborgroup</span></div>
  <p class="person">RHEA CALLOWAY<small>Director</small></p>
  <p class="c-left">1300 555 018<br>info@quillharborgroup.example<br>www.quillharborgroup.example</p>
  <p class="c-right">Level 12, Harbor Point<br>88 Quay Lane<br>Sydney NSW 2000</p>
</section>

<!-- Business card back -->
<section class="sheet card card-back">
  <div class="divider-v"></div><div class="divider-h"></div>
  <div class="grid">
    <div class="brand is-main"><span class="mark"></span><span class="name">quillharborgroup</span></div>
    <div class="brand is-teal" style="padding-left:6px"><span class="mark"></span><span class="name">tealridgefuelsales</span></div>
    <div class="brand is-orange"><span class="mark"></span><span class="name">orbvalechainsales</span></div>
    <div class="brand is-green" style="padding-left:6px"><span class="mark"></span><span class="name">pondgrovegrocerdeals</span></div>
  </div>
</section>

<!-- Envelope front -->
<section class="sheet envelope envelope-front">
  <div class="band red"></div><div class="band slate"></div>
  <div class="brand"><span class="mark"></span><span class="name">quillharborgroup</span></div>
  <p class="ret">Level 12, Harbor Point,<br>88 Quay Lane, Sydney NSW 2000</p>
</section>

<!-- Envelope back -->
<section class="sheet envelope envelope-back">
  <svg class="flap" viewBox="0 0 400 57" aria-hidden="true"><polygon points="0,0 400,0 388,57 12,57" fill="#34444e"/></svg>
  <span class="flap-mark"></span>
  <div class="area-strip">
    <div class="brand is-orange"><span class="mark"></span><span class="name">orbvalechainsales</span></div>
    <span class="sep"></span>
    <div class="brand is-teal"><span class="mark"></span><span class="name">tealridgefuelsales</span></div>
    <span class="sep"></span>
    <div class="brand is-green"><span class="mark"></span><span class="name">pondgrovegrocerdeals</span></div>
  </div>
</section>

</body>
</html>
```